Investment company needing business card

We are wanting a business card which looks sharp and easy on the eye. We are thinking of having a business card with the logo embossed on it, to really make it stand out. We will only have a small amount of information of the business card, person's name, position, email address and phone number

Danielle Hartig
Executive Assistant
+64 21 574 3162
danielleh@quarvendale.co.nz

Requirements
Must have
• Embossed logo
Should not have
• Not to be busy

```html
<!DOCTYPE html>
<html lang="en">
<head>
<meta charset="utf-8">
<title>Quarvendale Group – Business Card</title>
<link rel="stylesheet" href="https://fonts.googleapis.com/css2?family=Roboto+Condensed:wght@400;500&display=swap">
<style>
  :root {
    --backdrop: #e6e6e6;
    --card-white: #ffffff;
    --card-dark: #252525;
    --brand-green: #23b46e;
    --ink-grey: #555555;
    --band-grey: #676767;
    --emboss-grey: #9a9a9a;
  }
  * { margin: 0; padding: 0; box-sizing: border-box; }
  html, body {
    width: 1200px; height: 897px; overflow: hidden;
    background: var(--backdrop);
    font-family: "Roboto Condensed", sans-serif;
  }
  .card {
    position: absolute; left: 303px; width: 594px; height: 338px; overflow: hidden;
  }
  .card--front { top: 92px; background: var(--card-white); }
  .card--back { top: 469px; background: var(--card-dark); }

  .brand {
    position: absolute; display: flex; align-items: center; gap: 10px;
    font-weight: 500; letter-spacing: 0.5px; white-space: nowrap;
  }
  .brand__square { display: block; }
  .card--front .brand { left: 33px; top: 38px; font-size: 26px; color: var(--brand-green); }
  .card--front .brand__square { width: 40px; height: 40px; background: var(--brand-green); }
  .card--back .brand { left: 0; right: 0; top: 142px; justify-content: center; font-size: 38px; color: var(--emboss-grey); }
  .card--back .brand__square { width: 58px; height: 58px; background: #1c1c1c; }

  .person { position: absolute; right: 34px; top: 174px; text-align: right; }
  .person__name { font-size: 29px; font-weight: 400; color: var(--brand-green); line-height: 1.1; }
  .person__role { font-size: 14.5px; color: var(--ink-grey); margin-top: 3px; }

  .divider { position: absolute; left: 33px; right: 34px; top: 229px; height: 1.5px; background: var(--brand-green); }

  .contacts { position: absolute; left: 33px; top: 254px; list-style: none; }
  .contacts li {
    display: flex; align-items: center; gap: 9px;
    font-size: 14.5px; color: var(--ink-grey); height: 18.5px;
  }
  .contacts svg { width: 11px; height: 11px; flex: none; }

  .swoosh { position: absolute; left: 0; top: 0; }
</style>
</head>
<body>
  <section class="card card--front">
    <div class="brand"><span class="brand__square"></span>QUARVENDALE GROUP</div>

    <div class="person">
      <h1 class="person__name">DANIELLE HARTIG</h1>
      <p class="person__role">Executive Assistant</p>
    </div>

    <div class="divider"></div>

    <ul class="contacts">
      <li>
        <svg viewBox="0 0 12 12"><path d="M3 1 L5 3.5 L4 5 Q5 7.5 7 8 L8.5 7 L11 9 L9.5 11 Q3 10.5 1 2.5 Z" fill="var(--brand-green)"/></svg>
        +64 21 574 3162
      </li>
      <li>
        <svg viewBox="0 0 12 12"><rect x="1" y="2.5" width="10" height="7" fill="none" stroke="var(--brand-green)" stroke-width="1.2"/><path d="M1 2.5 L6 6.5 L11 2.5" fill="none" stroke="var(--brand-green)" stroke-width="1.2"/></svg>
        danielleh@quarvendale.co.nz
      </li>
      <li>
        <svg viewBox="0 0 12 12" fill="none" stroke="var(--brand-green)" stroke-width="1"><circle cx="6" cy="6" r="5"/><ellipse cx="6" cy="6" rx="2.2" ry="5"/><path d="M1 6 H11 M2 3.5 H10 M2 8.5 H10"/></svg>
        www.daniellehquarvendale.co.nz
      </li>
    </ul>

    <svg class="swoosh" width="594" height="338" viewBox="0 0 594 338">
      <path d="M222 338 Q360 290 594 293 L594 338 Z" fill="var(--brand-green)"/>
      <path d="M290 338 Q400 300 594 299 L594 338 Z" fill="var(--card-white)"/>
      <path d="M297 338 Q405 303 594 302 L594 338 Z" fill="var(--band-grey)"/>
    </svg>
  </section>

  <section class="card card--back">
    <div class="brand"><span class="brand__square"></span>QUARVENDALE GROUP</div>
  </section>
</body>
</html>
```